Crestline Marketing Business Card

Business card using new logo for marketing consulting company based in Silicon Valley. Limited information on card now (name, phone number, email, website), but room to add mailing address later.

```html
<!DOCTYPE html>
<html lang="en">
<head>
<meta charset="utf-8">
<title>Crestline Marketing – Business Card</title>
<link href="https://fonts.googleapis.com/css2?family=Open+Sans:wght@400;600;700&display=swap" rel="stylesheet">
<style>
  :root {
    --brand-cyan: #00ade0;
    --brand-sky: #1aa7dc;
    --frame-blue: #3aa9d8;
    --navy: #353c73;
    --rule-navy: #2e2f6e;
    --grey: #9a9ea5;
    --label: #231f20;
    --white: #ffffff;
  }
  * { margin: 0; padding: 0; box-sizing: border-box; }
  html, body { width: 900px; height: 1200px; overflow: hidden; background: var(--white); }
  body { font-family: "Open Sans", Arial, sans-serif; position: relative; }

  .sheet { position: absolute; left: 0; top: 0; width: 900px; height: 1200px; border: 1.5px solid var(--frame-blue); }

  .side-label { position: absolute; left: 48px; font-size: 34px; color: var(--label); font-weight: 400; line-height: 1; }
  .side-label--front { top: 30px; }
  .side-label--back { top: 618px; }

  /* Front */
  .card-front { position: absolute; left: 52px; top: 82px; width: 800px; height: 518px; border: 1.5px solid var(--frame-blue); background: var(--white); }
  .brand-name { position: absolute; left: 0; width: 100%; text-align: center; color: var(--brand-sky); font-weight: 400; white-space: nowrap; line-height: 1.2; }
  .card-front .brand-name { top: 146px; font-size: 38px; }
  .holder-name { position: absolute; left: 0; top: 254px; width: 100%; text-align: center; font-size: 25px; line-height: 34px; font-weight: 700; color: var(--navy); }
  .holder-role { position: absolute; left: 0; top: 294px; width: 100%; text-align: center; font-size: 23px; line-height: 32px; color: var(--grey); }
  .contact-band { position: absolute; left: 0; top: 379px; width: 100%; height: 117px; background: var(--brand-cyan); }
  .band-rule { position: absolute; top: 366px; width: 3px; height: 142px; background: var(--rule-navy); }
  .band-rule--left { left: 62px; }
  .band-rule--right { left: 735px; }
  .contact { position: absolute; top: 392px; font-size: 19px; line-height: 30px; color: var(--white); font-style: normal; white-space: nowrap; }
  .contact--left { left: 74px; }
  .contact--right { right: 67px; text-align: right; }

  /* Back */
  .card-back { position: absolute; left: 52px; top: 662px; width: 800px; height: 516px; background: var(--brand-cyan); overflow: hidden; }
  .glow-band { position: absolute; left: 0; top: 114px; width: 100%; height: 288px;
    background: radial-gradient(ellipse 300px 200px at 560px 120px, #ffffff 0%, #c9ecf8 35%, #6fcdee 70%, #2bb7e5 100%); }
  .decor-field { position: absolute; left: 0; top: 0; width: 380px; height: 100%;
    background: linear-gradient(90deg, rgba(53,60,115,0.35) 0%, rgba(255,255,255,0.25) 55%, rgba(255,255,255,0) 100%); }
  .card-back .brand-name { left: 380px; width: 360px; top: 278px; font-size: 30px; }
</style>
</head>
<body>
  <main class="sheet">
    <p class="side-label side-label--front">cm_front</p>
    <section class="card-front" aria-label="Business card front">
      <p class="brand-name">Crestline Marketing</p>
      <h1 class="holder-name">Name N. Name</h1>
      <p class="holder-role">DESIGNATION</p>
      <div class="contact-band"></div>
      <span class="band-rule band-rule--left"></span>
      <span class="band-rule band-rule--right"></span>
      <address class="contact contact--left">
        Phone:+123 456 7891<br>
        Mobile:+123 456 7891<br>
        email@crestline-marketing.net
      </address>
      <address class="contact contact--right">
        P.O. BOX 123 - 456, Silicon<br>
        Av, Silicon Valley<br>
        www.crestline-marketing.net
      </address>
    </section>

    <p class="side-label side-label--back">cm_Back</p>
    <section class="card-back" aria-label="Business card back">
      <div class="glow-band"></div>
      <div class="decor-field" role="img" aria-label="Decorative arrangement of large white and navy circles"></div>
      <p class="brand-name">Crestline Marketing</p>
    </section>
  </main>
</body>
</html>
```